Veterinary TPLO Surgery Flyer Design

Please use this flyer to make a professional-looking 1 page, double-sided client handout regarding TPLO.

You can visit our website at www.brackenfieldpetcare.com & www.northwoodsanimalsurgerygroup.com for additional logo information. The flyer should include all the text from the one provided.

Target Market(s)

Client communication to for referral surgery between sister veterinary clinics

Industry/Entity Type

Veterinary

Requirements
Must have
• The text included
Nice to have
• Nice to have the Cedar Hollow Avenue Animal CLinic & Dr. Pell Mobile vet logos incorporated.

```html
<!DOCTYPE html>
<html lang="en">
<head>
<meta charset="utf-8">
<title>TPLO Surgery Client Handout</title>
<link href="https://fonts.googleapis.com/css2?family=Outfit:ital,wght@0,300;0,400;0,500;0,600;0,700;1,600&display=swap" rel="stylesheet">
<style>
:root{
  --stage:#8f8f8f;
  --green:#4b8a63;
  --green-dark:#1e6a38;
  --green-head:#3f8a5c;
  --sky:#e7f3fa;
  --ink:#3a3a3a;
  --white:#ffffff;
  --pill-dark:#2f2f2f;
}
*{margin:0;padding:0;box-sizing:border-box}
html,body{width:1200px;height:800px;overflow:hidden}
body{background:var(--stage);font-family:'Outfit',sans-serif;color:var(--ink);position:relative}
.side-label{position:absolute;top:40px;color:var(--white);font-weight:700;font-size:22px;letter-spacing:10px}
.side-label.front{left:262px}
.side-label.back{left:861px}
.page{position:absolute;top:76px;width:517px;height:669px;background:var(--white);overflow:hidden}
.page.front{left:62px}
.page.back{left:631px}
.band{position:absolute;left:0;width:100%}
.abs{position:absolute}
.photo{position:absolute}
h2{font-weight:700;color:var(--green-head);font-size:17px;line-height:1.1}
p{font-weight:300;line-height:1.38}
.foot-bar{position:absolute;bottom:0;height:7px}
.foot-bar.a{left:0;width:256px;background:var(--green)}
.foot-bar.b{left:260px;width:257px;background:var(--green-dark)}

/* front hero */
.hero{top:0;height:138px;background:linear-gradient(90deg,#3f7a45 0%,#4f8a48 45%,#6d9a4a 70%,#8aae58 100%)}
.hero .photo{right:0;top:0;width:250px;height:138px;background:linear-gradient(135deg,#7ea055,#5d7f3a 50%,#a3b86a)}
.brand{left:29px;top:20px;display:flex;align-items:center;gap:6px;color:var(--white);font-size:12px;font-weight:400;line-height:1.1;width:170px}
.brand .dot{width:22px;height:22px;border-radius:50%;background:var(--white);flex:none}
.hero-title{left:29px;top:68px;color:var(--white);font-weight:700;font-size:14.3px;line-height:1.28;white-space:nowrap}

.about{top:138px;height:129px;background:var(--white)}
.about .photo{left:29px;top:11px;width:104px;height:104px;border-radius:8px;background:linear-gradient(180deg,#cfe4cf,#9cc7a3)}
.about h2{position:absolute;left:151px;top:17px}
.about p{position:absolute;left:151px;top:40px;width:345px;font-size:9.1px}

.tplo{top:267px;height:145px;background:var(--green)}
.tplo h2{position:absolute;left:31px;top:18px;color:var(--white);font-size:16px}
.tplo p{position:absolute;left:31px;top:43px;width:222px;font-size:9px;color:var(--white);line-height:1.3}
.tplo b{font-weight:600}
.tplo .photo{top:40px;height:80px;width:110px;border:1px solid var(--white);border-radius:3px}
.tplo .p1{left:267px;background:linear-gradient(135deg,#e6e4dc,#c9c6bc)}
.tplo .p2{left:384px;background:linear-gradient(135deg,#3a3a3a,#111)}

.benefits{top:412px;height:117px;background:var(--sky)}
.benefits h2{position:absolute;left:30px;top:18px}
.benefit{position:absolute;top:49px;display:flex;gap:6px}
.benefit .ring{width:41px;height:41px;border:1.3px solid var(--green);border-radius:50%;flex:none;display:flex;align-items:center;justify-content:center}
.benefit h3{font-size:8.5px;font-weight:600;margin-top:2px;color:#222}
.benefit p{font-size:7.4px;margin-top:3px;line-height:1.25}
.b1{left:28px;width:155px}.b2{left:190px;width:152px}.b3{left:343px;width:160px}

.why{top:529px;height:133px}
.why .photo{left:23px;top:-14px;width:80px;height:140px;border-radius:40px 40px 10px 10px;background:linear-gradient(180deg,#b77a44,#8e5428)}
.why h2{position:absolute;left:120px;top:20px}
.why p{position:absolute;left:122px;width:378px;font-size:9.1px}
.why .p-a{top:46px}
.why .p-b{top:88px;font-weight:500;color:#222}

/* back */
.bhero{top:0;height:138px;background:var(--green)}
.bhero .photo{right:0;top:0;width:175px;height:138px;background:linear-gradient(120deg,#8a7d72,#c9c2b8 50%,#a69a8e)}
.bhero h1{position:absolute;left:29px;top:22px;color:var(--white);font-size:16.3px;font-weight:700;line-height:1.25}
.bhero h1 span{color:#7fd39a}
.bhero p{position:absolute;left:29px;top:67px;width:305px;font-size:8.7px;color:var(--white);line-height:1.3}

.process{top:138px;height:256px;background:var(--sky)}
.process h2{position:absolute;left:30px;top:18px}
.step{position:absolute;display:flex;gap:8px;width:222px}
.step .ring{width:25px;height:25px;border:1px solid var(--green);border-radius:50%;flex:none;margin-top:1px;display:flex;align-items:center;justify-content:center}
.step p{font-size:9px;line-height:1.27}
.step b{font-weight:600;color:#222}
.l{left:30px}.r{left:262px}

.post{top:394px;height:275px}
.post h2{position:absolute;left:28px;top:14px;font-size:17px}
.post .sub{position:absolute;left:28px;top:38px;font-size:8.6px}
.pill{position:absolute;left:26px;width:137px;height:20px;border-radius:10px;color:var(--white);font-weight:600;font-size:12.5px;display:flex;align-items:center;gap:5px;padding-left:5px}
.pill.one{top:60px;background:var(--green)}
.pill.two{top:87px;background:var(--pill-dark)}
.pill-note{position:absolute;left:170px;width:170px;font-size:8.7px;line-height:1.27}
.note{position:absolute;left:28px;top:116px;width:305px;font-size:7.9px;font-style:italic;font-weight:600;color:var(--green-head);line-height:1.3}
.contact-title{position:absolute;left:26px;top:170px;font-size:16.5px;font-weight:600;color:#333;display:flex;align-items:center;gap:6px;width:310px}
.contact-title::after{content:"";flex:1;height:1px;background:var(--green)}
.contact-col{position:absolute;top:196px;font-size:7.4px;line-height:1.42;white-space:nowrap}
.contact-col h4{font-size:9.9px;font-weight:500;margin-bottom:3px;color:#222;line-height:1.22}
.contact-col.c1{left:28px;width:168px}
.contact-col.c2{left:199px;width:155px;border-left:1px dashed #999;padding-left:7px;height:68px}
.contact-col .tight{font-size:6.9px;letter-spacing:-0.1px}
.ic{display:inline-block;width:7px;height:7px;vertical-align:-1px;margin-right:3px}
.post .photo{left:356px;width:144px;border-radius:4px}
.post .ph1{top:20px;height:109px;background:linear-gradient(160deg,#c07a3a,#8a5a34 50%,#d8c7a4)}
.post .ph2{top:139px;height:109px;background:linear-gradient(160deg,#b9b6b0,#6f6c68 55%,#d6d3cd)}
</style>
</head>
<body>
<div class="side-label front">FRONT</div>
<div class="side-label back">BACK</div>

<section class="page front">
  <div class="band hero">
    <div class="photo" role="img" aria-label="Photo of a brown dog and a small child in a green forest"></div>
    <div class="abs brand"><span class="dot"></span><span>Cedar Hollow Avenue Animal Clinic</span></div>
    <div class="abs hero-title">Advanced Orthopedic Care by<br>Dr. Helena Pell, DVM, DNBVS-sa TPLO<br>Surgery at Cedar Hollow Avenue Animal Clinic</div>
  </div>

  <div class="band about">
    <div class="photo" role="img" aria-label="Illustrated badge with pine trees, sun and dog for the veterinary surgery specialist"></div>
    <h2>About Dr. Helena Pell</h2>
    <p>Dr. Helena Pell is a board-certified veterinary surgeon (Diplomate of the National Board of Veterinary Surgeons) with over 18 years of experience in small animal surgery. A graduate of Great Lakes State University, she completed her surgical residency at Harborview School of Veterinary Medicine. Through her mobile practice, Pell Mobile Surgery, Dr. Pell now provides advanced surgical procedures—such as TPLO—directly at local clinics.</p>
  </div>

  <div class="band tplo">
    <h2>What is TPLO Surgery?</h2>
    <p><b>Tibial Plateau Leveling Osteotomy (TPLO)</b> is a surgical procedure that stabilizes the stifle (knee) joint <b>following a cranial cruciate ligament (CCL)</b> rupture—a common orthopedic injury in dogs. The procedure involves altering the angle of the tibial plateau to eliminate abnormal joint motion, restoring stability and improving function.</p>
    <div class="photo p1" role="img" aria-label="Diagram of the knee joint before and after TPLO"></div>
    <div class="photo p2" role="img" aria-label="X-rays of a dog knee before and after TPLO"></div>
  </div>

  <div class="band benefits">
    <h2>Benefits of TPLO Surgery</h2>
    <div class="benefit b1">
      <div class="ring"><svg width="20" height="22" viewBox="0 0 20 22" fill="none" stroke="#4b8a63" stroke-width="1.3"><path d="M7 1v7M13 1v7M7 14v7M13 14v7M5 8h10v6H5z"/></svg></div>
      <div><h3>Enhanced Joint Stability</h3><p>Restores natural biomechanics, reducing pain and improving mobility.</p></div>
    </div>
    <div class="benefit b2">
      <div class="ring"><svg width="22" height="22" viewBox="0 0 22 22" fill="none" stroke="#4b8a63" stroke-width="1.3"><path d="M4 8a8 8 0 0 1 14-2M18 14a8 8 0 0 1-14 2M18 2v4h-4M4 20v-4h4M9 7h4v3h3v3h-3v3H9v-3H6v-3h3z"/></svg></div>
      <div><h3>Faster Recovery</h3><p>Many dogs return to normal activity faster compared to other surgical techniques.</p></div>
    </div>
    <div class="benefit b3">
      <div class="ring"><svg width="22" height="22" viewBox="0 0 22 22" fill="none" stroke="#4b8a63" stroke-width="1.3"><path d="M11 1l3 2.5 4-.3.7 3.9 3 2.6-2 3.4.4 3.9-3.9.9L11 21l-3.2-2.1-3.9-.9.4-3.9-2-3.4 3-2.6L6 3.2l4 .3z"/><path d="M7 11l3 3 5-6"/></svg></div>
      <div><h3>Proven Long-Term Success</h3><p>TPLO is particularly effective in large and active breeds</p></div>
    </div>
  </div>

  <div class="band why">
    <div class="photo" role="img" aria-label="Photo of a boxer dog wearing a stethoscope"></div>
    <h2>Why Choose Cedar Hollow Avenue Animal Clinic?</h2>
    <p class="p-a">Partnering with Dr. Pell, Cedar Hollow Avenue Animal Clinic offers advanced orthopedic surgery on-site—eliminating the need for referrals or travel. This collaboration ensures your pet receives expert surgical care in a familiar, trusted environment.</p>
    <p class="p-b">Our clinic works directly with your primary veterinarian to share medical records, diagnostics, and prescriptions, ensuring seamless and coordinated care for your pet</p>
  </div>
  <div class="foot-bar a"></div><div class="foot-bar b"></div>
</section>

<section class="page back">
  <div class="band bhero">
    <div class="photo" role="img" aria-label="Photo of a kitten resting on a blanket"></div>
    <h1>Diagnostic Radiographs <span>VS.</span><br>TPLO Planning Radiographs</h1>
    <p>While diagnostic radiographs may confirm a CCL tear, they are not sufficient for surgical planning. TPLO requires three advanced technique radiographic views with precise measurements, which must be performed under sedation to reduce discomfort and allow accurate positioning</p>
  </div>

  <div class="band process">
    <h2>Expected Process</h2>
    <div class="step l" style="top:54px"><div class="ring"><svg width="13" height="13" viewBox="0 0 13 13" fill="none" stroke="#4b8a63"><rect x="1" y="2" width="11" height="8"/><path d="M4 12h5"/></svg></div><p><b>Diagnosis:</b> Your pet is diagnosed with stifle instability (CCL tear) by your veterinarian.</p></div>
    <div class="step l" style="top:88px"><div class="ring"><svg width="13" height="13" viewBox="0 0 13 13" fill="none" stroke="#4b8a63"><path d="M3 2h7v9H3zM5 5h3M5 7h3"/></svg></div><p><b>Referral:</b> Your veterinarian contacts the surgical coordinator at Cedar Hollow Avenue Animal Clinic.</p></div>
    <div class="step l" style="top:133px"><div class="ring"><svg width="13" height="13" viewBox="0 0 13 13" fill="none" stroke="#4b8a63"><circle cx="6.5" cy="4" r="2"/><path d="M2 12c0-3 2-4.5 4.5-4.5S11 9 11 12"/></svg></div><p><b>Consultation:</b> The coordinator contacts you to schedule a 1-hour consultation to review the procedure, estimated costs, and available surgery dates.</p></div>
    <div class="step l" style="top:189px"><div class="ring"><svg width="13" height="13" viewBox="0 0 13 13" fill="none" stroke="#4b8a63"><rect x="2" y="1" width="9" height="11"/><path d="M6.5 3v7M4 5h5M4 8h5"/></svg></div><p><b>Planning Radiographs:</b> These specialized X-rays are typically taken during the consultation under light sedation.</p></div>
    <div class="step r" style="top:53px"><div class="ring"><svg width="13" height="13" viewBox="0 0 13 13" fill="none" stroke="#4b8a63"><rect x="1" y="3" width="11" height="7"/><path d="M3 6h7"/></svg></div><p><b>Surgical Review:</b> Dr. Pell reviews the radiographs and your pet’s medical history to confirm candidacy for TPLO.</p></div>
    <div class="step r" style="top:99px"><div class="ring"><svg width="13" height="13" viewBox="0 0 13 13" fill="none" stroke="#4b8a63"><circle cx="6.5" cy="6.5" r="4.5"/><path d="M6.5 3.5v6M5 5h2.5a1 1 0 0 1 0 2H5.5a1 1 0 0 0 0 2H8"/></svg></div><p><b>Deposit:</b> A $3,500 deposit secures Dr. Pell’s travel and surgery date. This is refundable if canceled at least 5 days prior to the scheduled procedure.</p></div>
    <div class="step r" style="top:155px"><div class="ring"><svg width="13" height="13" viewBox="0 0 13 13" fill="none" stroke="#4b8a63"><path d="M2 11l7-7 2 2-7 7zM9 4l2-2"/></svg></div><p><b>Surgery Day:</b> Your pet is dropped off in the morning and surgery is performed the same day.</p></div>
    <div class="step r" style="top:200px"><div class="ring"><svg width="13" height="13" viewBox="0 0 13 13" fill="none" stroke="#4b8a63"><path d="M2 6l4.5-4L11 6v6H2zM5 12V8h3v4"/></svg></div><p><b>Discharge:</b> You’ll receive a post-surgery update and your pet will go home that evening.</p></div>
  </div>

  <div class="band post">
    <h2>Post-Operative Care &amp; Follow-Up</h2>
    <p class="sub">Two follow-up appointments will be scheduled:</p>
    <div class="pill one"><svg width="15" height="15" viewBox="0 0 15 15"><circle cx="7.5" cy="7.5" r="7.5" fill="#fff"/><path d="M4 7.5l2.5 2.5L11 5" stroke="#4b8a63" stroke-width="1.8" fill="none"/></svg>4 Weeks Post-Op</div>
    <p class="pill-note" style="top:60px">Evaluate healing, refill medications, and address any questions.</p>
    <div class="pill two"><svg width="15" height="15" viewBox="0 0 15 15"><circle cx="7.5" cy="7.5" r="7.5" fill="#fff"/><path d="M4 7.5l2.5 2.5L11 5" stroke="#2f2f2f" stroke-width="1.8" fill="none"/></svg>8 Weeks Post-Op</div>
    <p class="pill-note" style="top:87px">Sedated radiographs will confirm proper healing of the surgical site and tibia.</p>
    <p class="note">Dr. Pell will stay in direct contact with you during your pet’s recovery using her custom mobile app, which allows for secure messaging and provides detailed post-operative instructions.</p>
    <div class="contact-title">Contact Information</div>
    <div class="contact-col c1">
      <h4>Cedar Hollow Avenue Animal Clinic</h4>
      <div><svg class="ic" viewBox="0 0 8 8"><path d="M4 0a3 3 0 0 1 3 3c0 2-3 5-3 5S1 5 1 3a3 3 0 0 1 3-3z" fill="#4b8a63"/></svg>2240 Cedar Hollow Avenue, Marlow, MI 48011</div>
      <div><svg class="ic" viewBox="0 0 8 8"><path d="M1 1h2l1 2-1 1a4 4 0 0 0 2 2l1-1 2 1v2C4 8 0 4 1 1z" fill="#4b8a63"/></svg>(555) 214-0387</div>
      <div><svg class="ic" viewBox="0 0 8 8" fill="none" stroke="#4b8a63" stroke-width=".8"><rect x=".5" y="1.5" width="7" height="5"/><path d="M.5 1.5L4 4.5l3.5-3"/></svg>info@brackenfieldpetcare.com</div>
      <div><svg class="ic" viewBox="0 0 8 8" fill="none" stroke="#4b8a63" stroke-width=".8"><circle cx="4" cy="4" r="3.5"/><path d="M.5 4h7M4 .5c-2 2-2 5 0 7M4 .5c2 2 2 5 0 7"/></svg>www.brackenfieldpetcare.com</div>
    </div>
    <div class="contact-col c2">
      <h4>Pell Mobile Surgery<br>(Dr. Helena Pell)</h4>
      <div><svg class="ic" viewBox="0 0 8 8"><path d="M1 1h2l1 2-1 1a4 4 0 0 0 2 2l1-1 2 1v2C4 8 0 4 1 1z" fill="#4b8a63"/></svg>(555) 308-4412</div>
      <div><svg class="ic" viewBox="0 0 8 8" fill="none" stroke="#4b8a63" stroke-width=".8"><rect x=".5" y="1.5" width="7" height="5"/><path d="M.5 1.5L4 4.5l3.5-3"/></svg>drpell@pellmobilesurgery.com</div>
      <div class="tight"><svg class="ic" viewBox="0 0 8 8" fill="none" stroke="#4b8a63" stroke-width=".8"><circle cx="4" cy="4" r="3.5"/><path d="M.5 4h7M4 .5c-2 2-2 5 0 7M4 .5c2 2 2 5 0 7"/></svg>www.northwoodsanimalsurgerygroup.com</div>
    </div>
    <div class="photo ph1" role="img" aria-label="Photo of a small terrier dog licking its nose"></div>
    <div class="photo ph2" role="img" aria-label="Photo of a tabby kitten lying on the floor"></div>
  </div>
  <div class="foot-bar a"></div><div class="foot-bar b"></div>
</section>
</body>
</html>
```